WP website design (Wrexfordale)

We need a wordpress design for an established auction and real estate company based in Viginia- "The Name That Closes!". The winning design will incorporate a professional color scheme with company logo in a clean layout. The design needs to consider that this will be developed on a responsive theme.
Industry/Entity Type
Real Estate
Requirements
Must have
- - - We will require winning designer to provide a layered PSD (Adobe photoshop) concept file, along with any non-standard font files used.
- Logo attached. Color scheme should compliment the logo colors; nothing flashy, rather more business oriented … subdued colors. Lighten up the burgundy color; not so dark on the background;
- Horizontal Navigation menu with these pages:
- Home - Upcoming Auctions - Appraisals - Past Auctions - Real Estate for Sale Sellers - Buyers - About Wrexfordale - Contact Us
- A slideshow element on the home page use stock of real estate for the initial image.
- Sidebar widgets to be included are: Email sign-up form - Featured Auctions - Testimonial widget - 'Our Videos' widget; Social media icons somewhere in layout (facebook, twitter, RSS, and Youtube, linkedIn), News & Events widget, "Special announcements" blog.
- Homepage content is text:
- Wrexfordale is "The name that closes!"
- Wrexfordale Auctioneers International is a premier, full service Auction Company specializing in the sale of commercial and residential real estate through the auction method. In the last 53 years, we have conducted thousands of auctions across the United States and several foreign countries.
- We bring our years of experience in auctioning homes, land, condominiums, industrial properties, retail buildings and development sites to help private individuals, corporations and financial institutions sell their property. In addition, we can assist you with liquidating estates, antiques, equipment and firearms collections.
- We have conducted thousands of auctions, assisting a wide range of companies both large and small achieve maximum value for their capital assets.
Nice to have
- Site will have drop down menus, please show what one will look like.
Should not have
- no gavels should be used in the design

```html
<!DOCTYPE html>
<html lang="en">
<head>
<meta charset="utf-8">
<title>Wrexfordale Auctioneers</title>
<link rel="stylesheet" href="https://fonts.googleapis.com/css2?family=Arimo:wght@400;700&family=Libre+Baskerville:ital@0;1&display=swap">
<style>
:root{
  --red:#c21f2b;
  --red-dark:#a8151f;
  --blue:#2a4387;
  --page:#f1f1f1;
  --panel:#efefef;
  --line:#dadada;
  --text:#2b2b2b;
  --footer:#252525;
}
*{box-sizing:border-box;margin:0;padding:0}
html,body{width:1155px;height:1200px;overflow:hidden}
body{background:var(--page);font-family:"Arimo",Arial,sans-serif;color:var(--text);position:relative}
.abs{position:absolute}
.serif{font-family:"Libre Baskerville",Georgia,serif;font-style:italic;font-weight:400}

/* header */
.brand{left:101px;top:46px;display:flex;align-items:center;gap:10px}
.brand-mark{width:26px;height:26px;background:var(--blue)}
.brand-name{font-family:"Arimo",Arial,sans-serif;font-weight:700;font-size:22px;color:var(--blue);white-space:nowrap}
.social-title{left:818px;top:26px;font-size:22px;color:#333}
.social{left:820px;top:67px;display:flex;gap:16px}
.social span{width:32px;height:32px;border-radius:4px;background:var(--blue)}
.social span:nth-child(2n){background:var(--red)}

/* nav */
.nav{left:98px;top:125px;width:959px;height:44px;background:var(--red);border-radius:6px 6px 0 0;display:flex}
.nav a{color:#fff;text-decoration:none;font-size:12.5px;font-weight:700;letter-spacing:.2px;display:flex;align-items:center;justify-content:center;border-right:1px solid var(--red-dark);height:44px}
.nav a:last-child{border-right:0}
.nav a.active{background:var(--blue)}
.dropdown{left:342px;top:169px;width:162px;background:var(--blue);box-shadow:0 2px 4px rgba(0,0,0,.25);z-index:3}
.dropdown a{display:block;color:#fff;font-size:12.5px;font-weight:700;padding:7px 17px 8px;border-bottom:1px solid #3b5499;text-decoration:none}
.dropdown a:last-child{border-bottom:0}

/* hero */
.hero{left:99px;top:171px;width:673px;height:294px;background:linear-gradient(180deg,#8fb2d6 0%,#b9c9d2 35%,#9a6e57 60%,#5e7a3b 100%)}
.hero-caption{left:91px;top:373px;width:669px;height:60px;background:rgba(50,50,50,.78);color:#fff;font-size:17px;line-height:23px;padding:6px 10px 0 17px}

/* featured */
.featured{left:773px;top:171px;width:283px;height:294px;background:#fff;border:1px solid var(--line)}
.featured-head{height:39px;background:var(--blue);color:#fff;font-size:21px;padding:7px 0 0 24px;margin-top:2px}
.featured-title{font-size:13px;margin:14px 0 0 20px}
.featured-photo{margin:8px 0 0 20px;width:243px;height:98px;border:2px solid #ddd;background:linear-gradient(180deg,#7fa6cf,#c8cfd3 55%,#6f8d4c)}
.featured-meta{font-size:12px;line-height:18px;margin:16px 0 0 22px;color:#333}
.featured-meta b{font-weight:700}
.featured-sub{font-size:13px;margin:6px 0 0 21px}
.featured-addr{font-size:12px;margin:4px 0 0 22px;color:#333}

/* listings */
.section-title{left:101px;top:488px;font-size:22px;color:var(--red)}
.card{left:98px;width:650px;height:258px;background:#f7f7f7;border:1px solid var(--line);border-top:0}
.card-head{height:39px;background:var(--blue);color:#fff;font-family:"Libre Baskerville",Georgia,serif;font-size:15px;letter-spacing:.3px;padding:11px 0 0 14px;border-radius:6px 6px 0 0;margin:0 -1px}
.thumb{position:absolute;left:11px;top:56px;width:122px;height:99px;background:#fff;border:1px solid var(--line);border-radius:4px;padding:8px 6px}
.thumb div{width:100%;height:100%;background:linear-gradient(180deg,#9fc0e0 0%,#d6dcdc 45%,#7e9c58 70%,#6f9444 100%)}
.summary{position:absolute;left:145px;top:56px;width:485px;height:100px;background:#fff;border:1px solid var(--line);border-radius:4px;padding:9px 7px;font-size:12px;line-height:17.5px;text-transform:uppercase;color:#333}
.summary .hi{color:var(--red);font-weight:700}
.summary b{font-weight:700}
.details{position:absolute;left:13px;top:175px;width:118px;height:33px;background:linear-gradient(180deg,#3a3a3a,#050505);border:2px solid #ccc;border-radius:6px;color:#fff;font-size:15px;display:flex;align-items:center;gap:10px;padding-left:10px;letter-spacing:.5px}
.info{position:absolute;left:145px;top:167px;width:485px;height:79px;background:#fff;border:1px solid var(--line);border-radius:4px;padding:9px 7px;font-size:13.5px;line-height:20px;color:#333}
.info b{font-weight:700}

/* sidebar */
.sidebar{left:773px;top:481px;width:284px;height:592px;background:var(--panel);border:1px solid var(--line)}
.side-title{font-size:21px;color:var(--red);margin:12px 0 0 14px}
.side-text{font-size:13px;line-height:17.5px;color:#333;margin:12px 0 0 15px;width:230px;letter-spacing:.2px}
.signup{display:flex;margin:12px 0 0 13px}
.signup .field{width:205px;height:29px;background:#fff;border:1px solid #ccc;font-size:12px;color:#555;padding:7px 7px}
.signup .join{width:50px;height:29px;background:var(--blue);color:#fff;font-weight:700;font-size:14px;border-radius:0 8px 8px 0;display:flex;align-items:center;justify-content:center;letter-spacing:.5px}
.rule{height:1px;background:#d4d4d4;margin:0 4px}
.video{margin:18px 0 0 8px;width:272px;height:186px;position:relative;background:linear-gradient(180deg,#2c6cb8,#86acd0 40%,#c2b9a6 65%,#6b6556)}
.video svg.play{position:absolute;left:108px;top:58px}
.video .bar{position:absolute;left:0;bottom:0;width:100%;height:19px;background:#111;display:flex;align-items:center;gap:8px;padding:0 8px;color:#bbb;font-size:9px}
.news{list-style:none;margin:10px 0 0 15px;width:255px}
.news li{font-size:12px;line-height:15.5px;color:#333;margin-bottom:9px}

/* footer */
.footer{left:0;top:1107px;width:1155px;height:93px;background:var(--footer)}
.footer-nav{left:105px;top:1126px;font-size:12.5px;color:#fff}
.footer-nav span{color:#aaa;margin:0 7px}
.copy{left:105px;top:1152px;font-size:12.5px;color:#fff}
.footer-brand{left:880px;top:1136px;display:flex;align-items:center;gap:8px}
.footer-brand .brand-mark{width:20px;height:20px;background:#777}
.footer-brand .brand-name{font-size:17px;color:#cfcfcf}
</style>
</head>
<body>

<header>
  <div class="abs brand">
    <span class="brand-mark"></span>
    <span class="brand-name">Wrexfordale Auctioneers</span>
  </div>
  <div class="abs social-title serif">Social Media</div>
  <div class="abs social" aria-label="Social media links">
    <span role="img" aria-label="Social link"></span>
    <span role="img" aria-label="RSS feed"></span>
    <span role="img" aria-label="Social link"></span>
    <span role="img" aria-label="Social link"></span>
    <span role="img" aria-label="Video channel"></span>
  </div>
</header>

<nav class="abs nav">
  <a style="width:75px">HOME</a>
  <a style="width:166px">UPCOMING AUCTIONS</a>
  <a class="active" style="width:145px">ONLINE AUCTIONS</a>
  <a style="width:118px">REAL ESTATE</a>
  <a style="width:98px">SERVICES</a>
  <a style="width:95px">ABOUT US</a>
  <a style="width:154px">AUCTION GALLERY</a>
  <a style="width:108px">CONTACT</a>
</nav>
<div class="abs dropdown">
  <a>Wrexfordale</a>
  <a>Auctioneers</a>
  <a>Auctioneers</a>
</div>

<div class="abs hero" role="img" aria-label="Photo of brick and sided suburban homes under a blue sky"></div>
<div class="abs hero-caption serif">We have conducted thousands of auctions, assisting a wide range of companies both large and small achieve maximum value for their capital assets.</div>

<aside class="abs featured">
  <div class="featured-head serif">Featured Auctions</div>
  <div class="featured-title">Multi Estate &amp; Consignment Auction</div>
  <div class="featured-photo" role="img" aria-label="Photo of an agent in a suit standing in front of a house"></div>
  <div class="featured-meta"><b>Start Date/ Time:</b> Saturday, April 13,<br>2013 At 10:00 Am</div>
  <div class="featured-sub">Multi Estate &amp; Consignment Auction</div>
  <div class="featured-addr">Linden Street, Marlow, IA 52690</div>
</aside>

<h2 class="abs section-title serif">Upcoming Auctions</h2>

<article class="abs card" style="top:526px">
  <div class="card-head">160± ACRES LAND NOBLE COUNTY, OK</div>
  <div class="thumb"><div role="img" aria-label="Photo of a two-story farmhouse on a lawn"></div></div>
  <div class="summary">Ashford area * crop &amp; timber<br><span class="hi">160± acres land noble county</span><b>, OK ~ Ashford area * crop &amp;<br>timber ~ excellent hunting</b><br>Seller: The Redbud Heritage Foundation of Oklahoma</div>
  <div class="details"><svg width="20" height="20" viewBox="0 0 20 20"><circle cx="8" cy="8" r="6" fill="#cfe3f5" stroke="#fff" stroke-width="2"/><line x1="12.5" y1="12.5" x2="18" y2="18" stroke="#ddd" stroke-width="3"/></svg>Details</div>
  <div class="info">Begins:&nbsp; Tuesday, March 12, 2013 at 10:00 AM CDT<br><b>Location:</b>&nbsp; See Directions<br>United States Ashford, OK 74690</div>
</article>

<article class="abs card" style="top:815px">
  <div class="card-head">160± ACRES LAND NOBLE COUNTY, OK</div>
  <div class="thumb"><div role="img" aria-label="Photo of a two-story farmhouse on a lawn"></div></div>
  <div class="summary">Ashford area * crop &amp; timber<br><span class="hi">160± acres land noble county</span><b>, OK ~ Ashford area * crop &amp;<br>timber ~ excellent hunting</b><br>Seller: The Redbud Heritage Foundation of Oklahoma</div>
  <div class="details"><svg width="20" height="20" viewBox="0 0 20 20"><circle cx="8" cy="8" r="6" fill="#cfe3f5" stroke="#fff" stroke-width="2"/><line x1="12.5" y1="12.5" x2="18" y2="18" stroke="#ddd" stroke-width="3"/></svg>Details</div>
  <div class="info">Begins:&nbsp; Tuesday, March 12, 2013 at 10:00 AM CDT<br><b>Location:</b>&nbsp; See Directions<br>United States Ashford, OK 74690</div>
</article>

<aside class="abs sidebar">
  <div class="side-title serif">Email Sign Up</div>
  <p class="side-text">Sign up to receive exclusive email updates for upcoming auctions</p>
  <div class="signup"><div class="field">Email Address</div><div class="join">Join</div></div>
  <div class="rule" style="margin-top:19px"></div>
  <div class="video" role="img" aria-label="Video still of a large stucco house with palm trees">
    <svg class="play" width="54" height="54" viewBox="0 0 54 54"><circle cx="27" cy="27" r="27" fill="rgba(0,0,0,.7)"/><polygon points="21,15 39,27 21,39" fill="#fff"/></svg>
    <div class="bar">
      <svg width="9" height="10"><polygon points="0,0 9,5 0,10" fill="#fff"/></svg>
      <svg width="92" height="8"><rect width="92" height="8" rx="4" fill="#555"/><rect width="8" height="8" rx="4" fill="#ddd"/></svg>
      <span>00:00 / 04:36</span>
    </div>
  </div>
  <div class="rule" style="margin-top:17px"></div>
  <div class="side-title serif" style="margin-top:10px">News &amp; Blog</div>
  <ul class="news">
    <li>Great Land Auction Companies Make All the Difference</li>
    <li>Great OK Farms for Sale at Auction Prices</li>
    <li>Farmland Auctions on Route 66</li>
    <li>Great Land Auction Companies Make All the Difference</li>
    <li>Great Land Auction Companies Make All the Difference</li>
  </ul>
</aside>

<footer class="abs footer"></footer>
<div class="abs footer-nav">Home<span>|</span>Upcoming Auctions<span>|</span>Online Auctions<span>|</span>Real Estate<span>|</span>Services<span>|</span>About Us<span>|</span>Auction Gallery<span>|</span>Contact</div>
<div class="abs copy">Copyright © 2013 - 2013 Wrexfordale auctioneers. All Rights Reserved</div>
<div class="abs footer-brand">
  <span class="brand-mark"></span>
  <span class="brand-name">Wrexfordale Auctioneers</span>
</div>

</body>
</html>
```